tamo rix

TAMO RIX mobile technology servicesPhone and tablet repairs, screens data recovery.

Industry/Entity Type

Data Recovery

Contact Information for Business Card

0431 587 612

Colors
33a6d7
f04a50
0a90cc
e34197

Requirements
Must have
• Gary plinth
Nice to have
• White background

```html
<!DOCTYPE html>
<html lang="en">
<head>
<meta charset="utf-8">
<title>TAMO RIX – Business Card</title>
<link rel="stylesheet" href="https://fonts.googleapis.com/css2?family=Bree+Serif&family=Nunito:wght@800&family=Quicksand:wght@500&display=swap">
<style>
  :root {
    --backdrop: #eef2f4;
    --card: #ffffff;
    --sky: #33a6d7;
    --ocean: #0a90cc;
    --coral: #f04a50;
    --magenta: #e34197;
  }
  * { margin: 0; padding: 0; box-sizing: border-box; }
  html, body {
    width: 1200px;
    height: 900px;
    overflow: hidden;
    background: var(--backdrop);
  }
  .card {
    position: absolute;
    left: 180px;
    top: 210px;
    width: 840px;
    height: 480px;
    background: var(--card);
    box-shadow: 0 2px 10px rgba(10, 144, 204, 0.12);
  }
  .phone-outline {
    position: absolute;
    inset: 0;
    width: 840px;
    height: 480px;
  }
  .brand-name {
    position: absolute;
    left: 150px;
    top: 112px;
    font-family: "Bree Serif", serif;
    font-weight: 400;
    font-size: 100px;
    line-height: 1;
    letter-spacing: -1px;
    color: var(--ocean);
  }
  .brand-tagline {
    position: absolute;
    left: 156px;
    top: 226px;
    font-family: "Nunito", sans-serif;
    font-weight: 800;
    font-size: 33px;
    line-height: 1;
    letter-spacing: -0.5px;
    color: var(--magenta);
  }
  .services {
    position: absolute;
    left: 130px;
    top: 346px;
    font-family: "Quicksand", sans-serif;
    font-weight: 500;
    font-size: 22px;
    line-height: 1.35;
    color: var(--ocean);
  }
  .contact {
    position: absolute;
    left: 530px;
    top: 282px;
    font-family: "Quicksand", sans-serif;
    font-weight: 500;
    font-size: 22px;
    line-height: 1.35;
    color: var(--ocean);
  }
  .contact-phone { color: var(--coral); }
</style>
</head>
<body>
  <div class="card">
    <svg class="phone-outline" viewBox="0 0 840 480" aria-hidden="true">
      <rect x="46" y="36" width="688" height="410" rx="22" fill="none" stroke="#33a6d7" stroke-width="3"/>
      <rect x="762" y="186" width="24" height="62" rx="12" fill="none" stroke="#33a6d7" stroke-width="3"/>
    </svg>
    <h1 class="brand-name">TAMO RIX</h1>
    <p class="brand-tagline">mobile technology services</p>
    <p class="contact">Contact info<br><span class="contact-phone">0431 587 612</span></p>
    <p class="services">Phone and tablet repairs,<br>screens data recovery.</p>
  </div>
</body>
</html>
```